Plakat-Design für Pfandhaus gesucht
Zielgruppe
Wir sind ein Pfandhaus wir vergeben Pfandkredite gegen Wertgegenstände sowie Juwelier und Goldankauf aber in erster Linie steht das Pfandhaus .
Aufgabenstellung
Ich möchte gerne Plakate Buchen die an Straßen oder Hauswänden befestigt sind. Ca.3,5x3 Meter. Die Botschaft muss kurz und knapp sein da die Leute ja vorbeifahren.

```html
<!DOCTYPE html>
<html lang="de">
<head>
<meta charset="utf-8">
<title>Pfandhaus Plakat</title>
<link href="https://fonts.googleapis.com/css2?family=Bebas+Neue&display=swap" rel="stylesheet">
<style>
  :root {
    --black: #000000;
    --white: #ffffff;
    --gold: #e8c64a;
    --gold-light: #f7e27a;
    --gold-dark: #b08a1e;
    --silver: #e6e6e6;
    --photo-gold-light: #f0cf6e;
    --photo-gold: #d2a23a;
    --photo-gold-dark: #7a5410;
  }
  html, body {
    margin: 0;
    padding: 0;
    overflow: hidden;
    background: var(--black);
  }
  .poster {
    position: relative;
    width: 848px;
    height: 1200px;
    background: var(--black);
    overflow: hidden;
    font-family: "Bebas Neue", "Arial Narrow", sans-serif;
  }
  .web-address {
    position: absolute;
    top: 22px;
    left: 0;
    width: 848px;
    text-align: center;
    color: var(--white);
    font-size: 72px;
    line-height: 1;
    letter-spacing: 1px;
  }
  .gold-stripe {
    position: absolute;
    top: 96px;
    left: 0;
    width: 848px;
    height: 27px;
    background: linear-gradient(180deg, var(--gold-light), var(--gold) 50%, var(--gold-dark));
  }
  .headline {
    position: absolute;
    top: 146px;
    left: 0;
    width: 848px;
    text-align: center;
    color: var(--white);
    font-size: 170px;
    line-height: 1;
    letter-spacing: 2px;
  }
  .metals {
    position: absolute;
    top: 322px;
    left: 119px;
    font-size: 160px;
    line-height: 1;
    white-space: nowrap;
  }
  .metals .gold {
    background: linear-gradient(180deg, var(--gold-light), var(--gold) 55%, var(--gold-dark));
    -webkit-background-clip: text;
    background-clip: text;
    color: transparent;
  }
  .metals .amp {
    color: var(--white);
    font-size: 100px;
    margin: 0 8px 0 12px;
  }
  .metals .silver {
    background: linear-gradient(180deg, var(--white), var(--silver) 60%, #b9b9b9);
    -webkit-background-clip: text;
    background-clip: text;
    color: transparent;
  }
  .cash-badge {
    position: absolute;
    left: 0;
    top: 560px;
    width: 460px;
    height: 470px;
  }
  .cash-text {
    position: absolute;
    left: 34px;
    top: 628px;
    width: 432px;
    text-align: center;
    color: var(--black);
  }
  .cash-text .line-s {
    display: block;
    font-size: 104px;
    line-height: 99px;
    letter-spacing: 3px;
  }
  .cash-text .line-l {
    display: block;
    font-size: 146px;
    line-height: 120px;
    margin-top: 4px;
    margin-left: -18px;
    letter-spacing: 1px;
  }
  .piggy-bank {
    position: absolute;
    left: 411px;
    top: 670px;
    width: 437px;
    height: 530px;
    border-radius: 60px 60px 0 0;
    background: radial-gradient(ellipse at 60% 40%, var(--photo-gold-light), var(--photo-gold) 50%, var(--photo-gold-dark));
  }
</style>
</head>
<body>
  <div class="poster">
    <div class="web-address">www.pfandhaus-lindenfeld.de</div>
    <div class="gold-stripe"></div>

    <div class="headline">PFANDHAUS</div>
    <div class="metals"><span class="gold">GOLD</span><span class="amp">&amp;</span><span class="silver">SILBER</span></div>

    <svg class="cash-badge" viewBox="0 0 460 470" aria-hidden="true">
      <defs>
        <linearGradient id="ringGold" x1="0" y1="0" x2="1" y2="1">
          <stop offset="0" stop-color="#f7e27a"/>
          <stop offset="0.5" stop-color="#e8c64a"/>
          <stop offset="1" stop-color="#b08a1e"/>
        </linearGradient>
      </defs>
      <circle cx="244" cy="230" r="208" fill="url(#ringGold)"/>
      <circle cx="225" cy="241" r="204" fill="#ffffff"/>
    </svg>
    <div class="cash-text">
      <span class="line-s">SOFORT-</span>
      <span class="line-s">GELD</span>
      <span class="line-l">IN BAR</span>
    </div>

    <div class="piggy-bank" role="img" aria-label="Foto: goldenes Sparschwein"></div>
  </div>
</body>
</html>
```